Business Card Design

Custom Injection Molding
Value Added Manufacturing
ISO 9001
Quality System Certified

Industry/Entity Type

Business

Contact Information for Business Card

Dorvane Polymers, Inc
Wendell Ashby
Purchasing Manager
2417 Halvers Lane
Lexington, KY 40511
Office 502-647-3918
Fax 502-613-4072
Mobile 502-788-2365

Requirements
Must have
• Colors
pantone blue 2145C
Brilliant White

Management wants to use attached logo design. Can you recreate it ?

```html
<!DOCTYPE html>
<html lang="en">
<head>
<meta charset="utf-8">
<title>Dorvane Polymers, Inc – Business Cards</title>
<link rel="stylesheet" href="https://fonts.googleapis.com/css2?family=Archivo+Black&family=Arimo:wght@400;700&display=swap">
<style>
  :root {
    --page-bg: #e6e4e1;
    --card-blue: #2f3c9e;
    --card-blue-deep: #26308a;
    --band-blue: #3545ad;
    --rule-cyan: #62c6ec;
    --white: #ffffff;
    --title-yellow: #f1e83a;
    --seal-green: #5fae5c;
    --seal-green-light: #a9dba3;
    --mark-green: #c4dc2a;
  }
  * { margin: 0; padding: 0; box-sizing: border-box; }
  html, body {
    width: 1200px; height: 1200px; overflow: hidden;
    background: var(--page-bg);
  }
  .sheet { position: relative; width: 1200px; height: 1200px; }

  .card {
    position: absolute;
    left: 136px;
    width: 928px; height: 542px;
    background: radial-gradient(ellipse at 50% 40%, var(--card-blue) 0%, var(--card-blue-deep) 100%);
    box-shadow: 0 6px 18px rgba(0,0,0,0.28);
    overflow: hidden;
    color: var(--white);
    font-family: "Arimo", Arial, sans-serif;
  }
  .card--plain { top: 43px; }
  .card--marked { top: 614px; }

  .brand-band {
    position: absolute; left: 0; top: 43px;
    width: 100%; height: 102px;
    background: var(--band-blue);
    border-top: 2px solid var(--rule-cyan);
    border-bottom: 2px solid var(--rule-cyan);
    display: flex; align-items: center; justify-content: center;
  }
  .brand-name {
    font-family: "Archivo Black", "Arial Black", sans-serif;
    font-size: 47px; line-height: 1;
    color: var(--white);
    letter-spacing: 0.5px;
    white-space: nowrap;
  }
  .card--marked .brand-band { justify-content: flex-start; padding-left: 44px; }
  .brand-dot {
    width: 84px; height: 84px; border-radius: 50%;
    background: var(--mark-green);
    margin-right: 26px; flex: none;
  }
  .card--marked .brand-name { font-size: 46px; }

  .services {
    position: absolute; left: 0; top: 158px; width: 100%;
    text-align: center;
    font-weight: 700; font-size: 22px; line-height: 34px;
  }

  .contact {
    position: absolute; left: 36px; top: 300px;
  }
  .contact-name {
    font-weight: 700; font-size: 37px; line-height: 44px;
    letter-spacing: 0.5px;
  }
  .contact-role {
    color: var(--title-yellow);
    font-size: 23px; line-height: 30px;
    margin-bottom: 14px;
  }
  .contact-lines { list-style: none; font-size: 22px; line-height: 32.5px; }

  .cert-seal {
    position: absolute; left: 726px; top: 342px;
    width: 172px; height: 172px;
  }
</style>
</head>
<body>
<main class="sheet">

  <section class="card card--plain" aria-label="Business card, version without mark">
    <header class="brand-band">
      <h1 class="brand-name">DORVANE POLYMERS, INC</h1>
    </header>
    <p class="services">Custom Injection Molding | Value Added Manufacturing<br>ISO 9001 Quality System Certified</p>
    <div class="contact">
      <h2 class="contact-name">WENDELL ASHBY</h2>
      <p class="contact-role">Purchasing Manager</p>
      <ul class="contact-lines">
        <li>2417 Halvers Lane Lexington, KY 40511</li>
        <li>Office: 502-647-3918</li>
        <li>Fax: 502-613-4072</li>
        <li>Mobile: 502-788-2365</li>
      </ul>
    </div>
    <svg class="cert-seal" viewBox="0 0 172 172" role="img" aria-label="Quality certification seal">
      <defs>
        <radialGradient id="seal-fill-a" cx="40%" cy="35%" r="70%">
          <stop offset="0" stop-color="var(--seal-green-light)"/>
          <stop offset="1" stop-color="var(--seal-green)"/>
        </radialGradient>
      </defs>
      <circle cx="86" cy="86" r="82" fill="url(#seal-fill-a)"/>
    </svg>
  </section>

  <section class="card card--marked" aria-label="Business card, version with mark">
    <header class="brand-band">
      <span class="brand-dot" aria-hidden="true"></span>
      <h1 class="brand-name">DORVANE POLYMERS, INC</h1>
    </header>
    <p class="services">Custom Injection Molding | Value Added Manufacturing<br>ISO 9001 Quality System Certified</p>
    <div class="contact">
      <h2 class="contact-name">WENDELL ASHBY</h2>
      <p class="contact-role">Purchasing Manager</p>
      <ul class="contact-lines">
        <li>2417 Halvers Lane Lexington, KY 40511</li>
        <li>Office: 502-647-3918</li>
        <li>Fax: 502-613-4072</li>
        <li>Mobile: 502-788-2365</li>
      </ul>
    </div>
    <svg class="cert-seal" viewBox="0 0 172 172" role="img" aria-label="Quality certification seal">
      <defs>
        <radialGradient id="seal-fill-b" cx="40%" cy="35%" r="70%">
          <stop offset="0" stop-color="var(--seal-green-light)"/>
          <stop offset="1" stop-color="var(--seal-green)"/>
        </radialGradient>
      </defs>
      <circle cx="86" cy="86" r="82" fill="url(#seal-fill-b)"/>
    </svg>
  </section>

</main>
</body>
</html>
```